RW Frameworks Inc Business cards

We need business cards using our existing logo but slightly modified. Right now the logo says RW Framework Masonry. We want to keep the RW part of the design, but replace the Framework Masonry portion with "FRAMEWORKS". Please see the attached file.
Ideally this would be a blank template so we can add Different Names, titles, and phone numbers later.
On the one side we want only the logo and on the other side the detail. I'm attaching an example for you to see.
Please reach out with any other questions. Our address and other details will be given out once we find a design we like.

Target Market(s)

Construction Industry

```html
<!DOCTYPE html>
<html lang="en">
<head>
<meta charset="utf-8">
<title>RW Frameworks Inc – Business Cards</title>
<link href="https://fonts.googleapis.com/css2?family=Exo+2:wght@600&family=Roboto:wght@400;500;700&display=swap" rel="stylesheet">
<style>
  :root {
    --brand-blue: #0f77bf;
    --brand-grey: #87888a;
    --text-grey: #555659;
    --card-white: #ffffff;
    --backdrop: #ececec;
  }
  * { margin: 0; padding: 0; box-sizing: border-box; }
  html, body {
    width: 1125px; height: 1200px; overflow: hidden;
    background: var(--backdrop);
    font-family: "Roboto", Arial, sans-serif;
  }
  .canvas { position: relative; width: 1125px; height: 1200px; }

  .card {
    position: absolute; left: 150px; width: 825px; height: 470px;
    box-shadow: 0 4px 14px rgba(0,0,0,0.18);
    overflow: hidden;
  }
  .card--front { top: 98px; background: var(--card-white); }
  .card--back { top: 632px; background: var(--brand-blue); }

  .wordmark {
    position: absolute;
    font-family: "Roboto", Arial, sans-serif;
    font-weight: 500;
    white-space: nowrap;
    letter-spacing: 1px;
  }
  .card--front .wordmark {
    left: 110px; top: 210px; font-size: 40px; color: var(--brand-blue);
  }
  .card--back .wordmark {
    left: 0; right: 0; top: 210px; text-align: center;
    font-size: 48px; color: var(--card-white);
  }

  .divider {
    position: absolute; left: 433px; top: 150px;
    width: 1px; height: 172px; background: #9a9b9d;
  }

  .details { position: absolute; left: 470px; top: 140px; }
  .details__name {
    font-family: "Exo 2", "Roboto", sans-serif; font-weight: 600;
    font-size: 26px; color: var(--brand-blue); letter-spacing: 0.3px;
  }
  .details__title {
    font-weight: 700; font-size: 17px; color: var(--brand-grey);
    margin-top: 2px; margin-left: 3px;
  }
  .contact-list { list-style: none; margin-top: 28px; margin-left: 5px; }
  .contact-list li {
    display: flex; align-items: center; height: 23.5px;
    font-size: 17.5px; color: var(--text-grey);
  }
  .contact-list svg { width: 15px; height: 15px; margin-right: 9px; fill: var(--brand-blue); flex: none; }

  .edge-band { position: absolute; left: 0; bottom: 0; width: 825px; height: 10px; }
</style>
</head>
<body>
<main class="canvas">

  <section class="card card--front" aria-label="Front of card">
    <div class="wordmark">RW Frameworks</div>
    <div class="divider"></div>

    <div class="details">
      <div class="details__name">DANIEL HARPER</div>
      <div class="details__title">President</div>
      <ul class="contact-list">
        <li>
          <svg viewBox="0 0 16 16" aria-hidden="true"><path d="M3.6 1.2l2.3 2.6-1.3 2a9 9 0 0 0 5.6 5.6l2-1.3 2.6 2.3-1.4 2.3C7.2 15.8.2 8.8 1.3 2.6z"/></svg>
          555-214-7730
        </li>
        <li>
          <svg viewBox="0 0 16 16" aria-hidden="true"><path d="M4.5 0.5h7a1 1 0 0 1 1 1v13a1 1 0 0 1-1 1h-7a1 1 0 0 1-1-1v-13a1 1 0 0 1 1-1zm0.8 2v9.5h5.4V2.5zM8 12.8a0.9 0.9 0 1 0 0 1.8a0.9 0.9 0 0 0 0-1.8z"/></svg>
          555-348-9162
        </li>
        <li>
          <svg viewBox="0 0 16 16" aria-hidden="true"><path d="M1 4h14v9H1zm1.2 1.1v0.4L8 9.3l5.8-3.8v-0.4z"/></svg>
          info@rwframeworks.com
        </li>
        <li>
          <svg viewBox="0 0 16 16" aria-hidden="true"><circle cx="8" cy="8" r="7"/><path d="M4 4.5c1.5 0 2.5 1 2 2.2s-1.8 1-1.6 2.5-1 1.5-1.6 1M10 2.5c-.5 1.2.8 1.8 1.8 1.6s1.8 1 1 2.2M9 14.5c0-1.5 1.3-2 1.3-3.3s1.6-1.3 2.5-.7" fill="none" stroke="#fff" stroke-width="1.2"/></svg>
          www.rwframeworks.com
        </li>
      </ul>
    </div>

    <svg class="edge-band" viewBox="0 0 825 10" preserveAspectRatio="none" aria-hidden="true">
      <polygon points="0,0 533,0 528,10 0,10" fill="var(--brand-blue)"/>
      <polygon points="538,0 825,0 825,10 533,10" fill="var(--brand-grey)"/>
    </svg>
  </section>

  <section class="card card--back" aria-label="Back of card">
    <div class="wordmark">RW Frameworks</div>
  </section>

</main>
</body>
</html>
```